High End Skincare for Women Cosmetics Brand

We need a wordpress website that is also a mobile-friendly website for our cosmetics company. We have 3 core products and have 10 dropship products to add. I have attached the pdf with brand guide and vision for the website.

Our mission - At Mira Vale we believe all women have four distinct characteristics; beauty, originality, passion, and confidence. Our beauty products simply enhance those qualities. We will always provide the safest products to our consumers and continue to uplift women around the world.

About us - MIRA VALE IS AN ORGANIC COSMETICS AND SKINCARE BRAND WITH VARIOUS PRODUCTS TO ENHANCE YOUR NATURAL BEAUTY. WE ARE COMMITTED TO PROVIDING TIMELESS PRODUCTS THAT WILL BRING OUT THAT SPECIAL CONFIDENCE YOU FEEL AND DESIRE FROM COSMETICS THAT WILL PERFECTLY MESH YOUR LIFESTYLE. When you choose Mira Vale organic cosmetics and skincare products, you are choosing a product whose ingredients work perfectly with the most complicated natural skin. We want you to celebrate that unique natural beauty with Mira Vale organic cosmetics and skincare products that will enhance your beauty. We use the best quality plant-based and laboratory-made ingredients to produce the best organic products that will enhance your beauty and boost your confidence.

XoXo Mira Vale - We understand that beauty is much more than an outward appearance. Our unique products bring you confidence, courage, and enrich your spirit. True beauty is deeper, and we at Mira Vale seek to inspire you to discover that deep sense of beauty you always craved.

Style - Luxury High End / Should look expensive and feminine with a modern touch.
The logo files are attached to this.

Colors should be bold and bright that looks like luxury and modern.

The products we sell are organic skincare and cosmetic products.

The design should not include any images or generic types of a font that can be found in Microsoft Word.

Premium font required.

Mira Vale is a leading organic cosmetics and skincare brand with products that enhance the natural beauty of the everyday woman. Luxury without the luxe price tag.

Target Market(s)

Target audience women age 18- 42 Gen Y / Millennials / Gen X

Industry/Entity Type

Beauty

Number of Pages Required

4 page

Font styles to use
Sans Serif

Colors

Designer to choose colors to be used in the design.

Requirements
Must have
• Must have images of women of diverse ethnicity at least 4 women
• Must have images of products -
• Must have an option to integrate dropship product links
• Must have contact us form
• Must have about us page
• Must have high-resolution images
• Must have a feature to check out on the website
• Must be mobile friendly
Nice to have
• Nice to have blog feature
• Nice to have a chat bot

```html
<!DOCTYPE html>
<html lang="en">
<head>
<meta charset="utf-8">
<title>Mira Vale — Organic Cosmetics &amp; Skincare</title>
<link href="https://fonts.googleapis.com/css2?family=Josefin+Sans:wght@100;300;400;600&family=Roboto:wght@300;400;500;700&family=Great+Vibes&display=swap" rel="stylesheet">
<style>
:root{
  --pink:#f47c9c;
  --pink-dark:#e8607f;
  --pink-soft:#f6dfe4;
  --gold:#c9a45f;
  --ink:#2b2b2b;
  --grey:#777;
  --light:#f5f5f5;
  --line:#e6e6e6;
  --dark:#1b1b1b;
  --footer:#2f2f2f;
  --white:#fff;
}
*{margin:0;padding:0;box-sizing:border-box}
html,body{width:1200px;height:4380px;overflow:hidden;background:var(--white)}
body{position:relative;font-family:'Roboto',sans-serif;color:var(--ink)}
.abs{position:absolute}
.section{position:absolute;left:0;width:1200px;overflow:hidden}
.img-fill{position:absolute}
.btn{position:absolute;height:36px;border-radius:18px;background:var(--pink);color:var(--white);font:500 14px/36px 'Roboto',sans-serif;text-align:center}
.center{text-align:center;left:0;width:1200px}

/* header */
.site-header{top:0;height:200px;background:var(--white)}
.logo{left:88px;top:34px;font:100 46px/1 'Josefin Sans',sans-serif;letter-spacing:14px;color:var(--ink)}
.nav-rule{left:88px;width:1024px;height:1px;background:var(--line)}
.main-nav{left:90px;top:148px;display:flex;font:400 14px 'Josefin Sans',sans-serif;color:var(--grey)}
.main-nav span{padding:0 14px;border-right:1px solid var(--line);line-height:22px;white-space:nowrap}
.main-nav span:last-child{border-right:0}
.main-nav .caret{padding:0;border:0;font-size:9px;color:var(--ink);margin-left:8px}
.main-nav .active{color:var(--gold)}

/* hero */
.hero{top:200px;height:422px;background:#111}
.hero-title{left:528px;top:44px;font:300 46px/56px 'Josefin Sans',sans-serif;letter-spacing:4px;color:var(--white)}
.hero-title .accent{color:var(--pink)}
.hero-arrow{width:36px;height:36px;background:var(--gold);top:194px}

/* about */
.about{top:622px;height:473px;background:var(--white)}
.section-title{font:100 52px/1 'Josefin Sans',sans-serif;letter-spacing:2px;color:#c9c9c9}
.section-title .cap{color:var(--pink);font-size:88px;font-weight:300}
.about-lead{top:170px;font:700 14px 'Roboto',sans-serif}
.about-sub{top:196px;font:400 13px 'Roboto',sans-serif;color:var(--grey)}
.about-text{left:335px;width:530px;font:300 12px/19px 'Roboto',sans-serif;color:var(--grey);text-align:center}

/* products */
.products{top:1095px;height:505px}
.product-tile{top:131px;width:234px;height:234px}

/* appointment */
.appointment{top:1600px;height:672px;background:var(--light)}
.booking-card{left:593px;top:64px;width:502px;height:555px;background:var(--white);box-shadow:0 2px 14px rgba(0,0,0,.08)}
.booking-banner{left:593px;top:64px;width:502px}
.booking-title{left:593px;width:502px;top:112px;text-align:center;color:var(--white);font:400 30px 'Roboto',sans-serif}
.booking-sub{left:593px;width:502px;top:158px;text-align:center;color:var(--white);font:400 13px 'Roboto',sans-serif}
.field{position:absolute;height:50px;border:1px solid var(--line);background:#f7f7f7;font:400 12px/50px 'Roboto',sans-serif;color:#999;padding-left:14px}

/* services */
.services{top:2272px;height:618px;background:var(--pink-soft)}
.script{font:400 30px 'Great Vibes',cursive;color:var(--pink)}
.services-title{top:110px;font:500 28px 'Roboto',sans-serif;letter-spacing:1px;color:#3a3a3a}
.services-text{top:156px;font:300 13px/21px 'Roboto',sans-serif;color:var(--grey)}
.service-card{left:0;top:257px;width:890px;height:361px;background:var(--white)}
.avatar{width:94px;height:94px;border-radius:50%}
.service-copy{left:290px;width:296px;text-align:center}
.dot{width:16px;height:16px;border-radius:50%}

/* contact */
.contact{top:2890px;height:590px;background:#222}
.contact-title{top:86px;font:500 34px 'Roboto',sans-serif;color:var(--white)}
.contact-info{left:137px;color:var(--white);font:400 14px/22px 'Roboto',sans-serif}
.input-dark{position:absolute;background:rgba(255,255,255,.18);border-radius:6px;color:#ddd;font:400 13px 'Roboto',sans-serif;padding:16px}

/* map */
.map{top:3480px;height:392px}

/* newsletter */
.newsletter{top:3872px;height:94px;background:var(--pink)}
.newsletter-text{left:137px;top:36px;color:var(--white);font:500 20px 'Roboto',sans-serif}
.news-input{left:748px;top:24px;width:262px;height:48px;background:#f9a8bd;color:var(--white);font:400 13px/48px 'Roboto',sans-serif;padding-left:16px;border-radius:4px 0 0 4px}
.news-btn{left:1010px;top:24px;width:114px;height:48px;background:var(--pink-dark);color:var(--white);font:500 15px/48px 'Roboto',sans-serif;text-align:center;border-radius:0 4px 4px 0}

/* footer */
.site-footer{top:3966px;height:379px;background:var(--footer);color:#ddd}
.footer-brand{left:137px;top:40px;font:400 34px 'Josefin Sans',sans-serif;color:var(--white)}
.footer-about{left:137px;top:104px;width:270px;font:300 13px/20px 'Roboto',sans-serif}
.social{top:218px;width:26px;height:26px;border-radius:50%;background:var(--white)}
.footer-heading{top:44px;font:500 22px 'Roboto',sans-serif;color:var(--white)}
.footer-nav{left:566px;top:102px;font:400 13px/22px 'Roboto',sans-serif}
.post-date{color:var(--pink);font:400 12px 'Roboto',sans-serif}
.post-text{font:400 13px/18px 'Roboto',sans-serif;color:#ddd}
.copyright{top:4345px;height:35px;background:#222;color:#777;font:400 11px/35px 'Roboto',sans-serif;text-align:center}
</style>
</head>
<body>

<header class="section site-header">
  <div class="abs logo">MIRA VALE</div>
  <svg class="abs" style="left:966px;top:54px" width="16" height="16" viewBox="0 0 16 16"><circle cx="6.5" cy="6.5" r="5" fill="none" stroke="#999" stroke-width="1.6"/><line x1="10.5" y1="10.5" x2="15" y2="15" stroke="#999" stroke-width="1.6"/></svg>
  <svg class="abs" style="left:1016px;top:52px" width="20" height="18" viewBox="0 0 20 18"><path d="M1 2h3l2 10h11l2-7H5" fill="none" stroke="#555" stroke-width="1.6"/><circle cx="8" cy="15.5" r="1.5" fill="#555"/><circle cx="15" cy="15.5" r="1.5" fill="#555"/></svg>
  <div class="abs" style="left:1030px;top:44px;width:14px;height:14px;border-radius:50%;background:var(--ink);color:#fff;font:400 9px/14px 'Roboto',sans-serif;text-align:center">0</div>
  <div class="abs" style="left:1062px;top:54px;font:400 13px 'Roboto',sans-serif;color:var(--gold)">$0.00</div>
  <div class="abs nav-rule" style="top:130px"></div>
  <nav class="abs main-nav">
    <span class="active">Home</span>
    <span>About Us<span class="caret">▼</span></span>
    <span>Blog<span class="caret">▼</span></span>
    <span>Portfolio<span class="caret">▼</span></span>
    <span>Shop<span class="caret">▼</span></span>
    <span>Shortcodes<span class="caret">▼</span></span>
    <span>Contact Us</span>
  </nav>
</header>

<section class="section hero">
  <div class="img-fill" role="img" aria-label="Woman applying mascara on a dark background" style="left:0;top:0;width:1200px;height:422px;background:linear-gradient(90deg,#d9c4b8 0%,#8e6f63 18%,#2a2222 32%,#111 50%,#161616 100%)"></div>
  <div class="img-fill" role="img" aria-label="Makeup brushes and mascara in a circular close-up" style="left:780px;top:150px;width:240px;height:240px;border-radius:50%;background:radial-gradient(circle at 40% 40%,#6b5a5a,#2a2424 70%)"></div>
  <div class="abs hero-title"><span class="accent">YOUR SKIN WILL</span><br>LOVE IT</div>
  <div class="abs hero-arrow" style="left:52px"><svg width="36" height="36"><path d="M21 12l-6 6 6 6" fill="none" stroke="#fff" stroke-width="2"/></svg></div>
  <div class="abs hero-arrow" style="left:1112px"><svg width="36" height="36"><path d="M15 12l6 6-6 6" fill="none" stroke="#fff" stroke-width="2"/></svg></div>
</section>

<section class="section about">
  <div class="img-fill" role="img" aria-label="Loose face powder and brush" style="left:0;top:0;width:220px;height:225px;background:radial-gradient(circle at 30% 40%,#e9cbb6,#f6e6dc 55%,rgba(255,255,255,0) 75%)"></div>
  <div class="img-fill" role="img" aria-label="Polaroid portrait photo" style="left:812px;top:52px;width:140px;height:140px;background:#f1ece8;border:8px solid #fff;box-shadow:0 2px 10px rgba(0,0,0,.2);transform:rotate(6deg)"></div>
  <div class="img-fill" role="img" aria-label="Red flowers and makeup brush" style="left:935px;top:341px;width:265px;height:103px;background:radial-gradient(ellipse at 60% 50%,#e47a86,#f3c6cc 50%,rgba(255,255,255,0) 75%)"></div>
  <div class="abs center section-title" style="top:64px"><span class="cap">A</span>BOUT US</div>
  <div class="abs center about-lead">Neque porro quisquam est qui dolorem ipsum quia dolor sit amet</div>
  <div class="abs center about-sub">There is no one who loves pain itself, who seeks</div>
  <p class="abs about-text" style="top:224px">Our organic formulas are blended from gentle plant extracts and pure minerals, made to care for every skin type. Each product is tested with care, so you can enjoy a soft glow from morning to night, day after day.</p>
  <p class="abs about-text" style="top:287px">We craft timeless skincare and cosmetics that bring out your natural confidence. Every formula is made to mesh with your lifestyle, giving you luxury care without the luxe price tag for every season.</p>
  <div class="btn" style="left:527px;top:360px;width:146px">Read Our Story</div>
</section>

<section class="section products">
  <div class="abs center section-title" style="top:40px"><span class="cap">O</span>UR PRODUCTS</div>
  <div class="img-fill product-tile" role="img" aria-label="Cream tube with white roses" style="left:93px;background:linear-gradient(160deg,#d7e6f2,#9fb9d1)"></div>
  <div class="img-fill product-tile" role="img" aria-label="Red skincare jars with pink lotus" style="left:350px;background:linear-gradient(160deg,#f7c4c4,#e05a6e)"></div>
  <div class="img-fill product-tile" role="img" aria-label="Golden serum bottle" style="left:613px;background:linear-gradient(160deg,#f6cf8e,#d9892f)"></div>
  <div class="img-fill product-tile" role="img" aria-label="Moisturiser tube in water splash" style="left:876px;background:linear-gradient(160deg,#bfe6f6,#3fa2d6)"></div>
  <div class="btn" style="left:527px;top:425px;width:146px">Show More</div>
</section>

<section class="section appointment">
  <div class="img-fill" role="img" aria-label="Smiling woman with arms crossed in a blue shirt" style="left:102px;top:50px;width:423px;height:622px;background:linear-gradient(180deg,#e9e3de 0%,#c9a287 30%,#5f7ea8 60%,#48648f 100%);border-radius:200px 200px 0 0"></div>
  <div class="abs booking-card"></div>
  <svg class="abs booking-banner" width="502" height="150" viewBox="0 0 502 150"><path d="M0 0H502V120L251 146L0 120Z" fill="#f47c9c"/></svg>
  <div class="abs booking-title">BOOK AN APPOINTMENT</div>
  <div class="abs booking-sub">Neque porro quisquam est qui dolorem ipsum quia dolor sit amet</div>
  <div class="field" style="left:613px;top:269px;width:225px">Name</div>
  <div class="field" style="left:853px;top:269px;width:222px">Date
    <svg class="abs" style="right:12px;top:17px" width="16" height="16"><rect x="1" y="3" width="14" height="12" fill="none" stroke="#999"/><line x1="1" y1="7" x2="15" y2="7" stroke="#999"/></svg></div>
  <div class="field" style="left:613px;top:333px;width:225px">Time<span class="abs" style="right:14px;top:0">⌄</span></div>
  <div class="field" style="left:853px;top:333px;width:222px">Appointment is for<span class="abs" style="right:14px;top:0">⌄</span></div>
  <div class="field" style="left:613px;top:403px;width:462px;height:94px;line-height:36px">Comment or questions</div>
  <div class="btn" style="left:759px;top:537px;width:190px;height:38px;line-height:38px;border-radius:19px">Book Now</div>
</section>

<section class="section services">
  <div class="img-fill" role="img" aria-label="Pink orchid flowers" style="left:0;top:0;width:380px;height:300px;background:radial-gradient(ellipse at 40% 40%,#f2a6c0,#f7cdd8 45%,rgba(246,223,228,0) 75%)"></div>
  <div class="abs center script" style="top:64px">Experience the art of caring</div>
  <div class="abs center services-title">VARIETY OF MAKEUP</div>
  <div class="abs center services-text">Non numquam eius modi tempora incidunt ut labore et dolore magnam aliquam<br>voluptatem. Ut enim ad minima veniam, quis nostrum</div>
  <div class="abs service-card"></div>
  <div class="img-fill avatar" role="img" aria-label="Portrait of a client" style="left:110px;top:280px;background:#3b3030"></div>
  <div class="img-fill avatar" role="img" aria-label="Portrait of a client" style="left:110px;top:390px;background:#c79c7f"></div>
  <div class="img-fill avatar" role="img" aria-label="Portrait of a client" style="left:110px;top:500px;background:#7a5a4a"></div>
  <div class="abs service-copy script" style="top:316px;font-size:24px">Looking for a beauty</div>
  <div class="abs service-copy" style="top:356px;font:400 13px 'Roboto',sans-serif;color:#444">WARM GOLD EYESSHADOW BRIDAL MAKEUP</div>
  <div class="abs service-copy" style="top:396px;font:400 13px 'Roboto',sans-serif;color:#444">$25.00 / PER HEAD</div>
  <div class="abs service-copy" style="top:422px;font:300 12px/18px 'Roboto',sans-serif;color:var(--grey)">Lorem ipsum dolor sit amet, consectetur adipisicing elit. Laudantium quas alias recusandae maiores excepturi quia minima, perferendis recusandae harum sit earum.</div>
  <div class="btn" style="left:313px;top:530px;width:250px;height:40px;line-height:40px;border-radius:20px">See All Services</div>
  <div class="img-fill" role="img" aria-label="Makeup artist applying eyeshadow, video preview" style="left:628px;top:321px;width:470px;height:234px;background:linear-gradient(90deg,#4a4140,#a98f86 45%,#6a5a58)"></div>
  <svg class="abs" style="left:838px;top:413px" width="50" height="50"><circle cx="25" cy="25" r="23" fill="rgba(255,255,255,.85)"/><path d="M20 15l14 10-14 10z" fill="#555"/></svg>
  <div class="abs dot" style="left:1043px;top:576px;background:var(--pink)"></div>
  <div class="abs dot" style="left:1078px;top:576px;background:var(--ink)"></div>
</section>

<section class="section contact">
  <div class="img-fill" role="img" aria-label="Close-up of a woman with closed eyes and purple flowers, darkened" style="left:0;top:0;width:1200px;height:590px;background:linear-gradient(120deg,#3a302e,#1c1818 40%,#2b2424 70%,#3a2a3a)"></div>
  <div class="abs center contact-title">CONTACT US</div>
  <div class="abs contact-info" style="top:190px;width:360px;font-size:14px">Non numquam eius modi tempora incidunt ut labore et doloremagnamaliqua voluptatem.</div>
  <svg class="abs" style="left:137px;top:255px" width="20" height="26"><path d="M10 1a8 8 0 0 0-8 8c0 6 8 16 8 16s8-10 8-16a8 8 0 0 0-8-8z" fill="#fff"/><circle cx="10" cy="9" r="3" fill="#222"/></svg>
  <div class="abs contact-info" style="left:193px;top:256px">418 Harbor Lane, Fairhaven, CA 90210</div>
  <svg class="abs" style="left:135px;top:312px" width="26" height="26"><circle cx="13" cy="13" r="11" fill="none" stroke="#fff" stroke-width="2"/><path d="M13 6v7l5 3" fill="none" stroke="#fff" stroke-width="2"/></svg>
  <div class="abs contact-info" style="left:193px;top:308px">Monday – Saturday<br>from 8:00 to 20:00</div>
  <svg class="abs" style="left:135px;top:386px" width="28" height="22"><path d="M2 8c6-7 18-7 24 0l-4 3-3-3H9l-3 3z" fill="#fff"/><rect x="6" y="11" width="16" height="10" rx="2" fill="#fff"/></svg>
  <div class="abs contact-info" style="left:193px;top:386px">555 – 014 – 2873</div>
  <div class="input-dark" style="left:564px;top:176px;width:274px;height:50px">Name</div>
  <div class="input-dark" style="left:853px;top:176px;width:271px;height:50px">Email</div>
  <div class="input-dark" style="left:564px;top:249px;width:560px;height:190px">Message</div>
  <div class="btn" style="left:768px;top:474px;width:184px;height:40px;line-height:40px;border-radius:20px">Send</div>
</section>

<section class="section map">
  <div class="img-fill" role="img" aria-label="Street map of the studio area" style="left:0;top:0;width:1200px;height:392px;background:linear-gradient(135deg,#e6ecd9,#f1efe6 40%,#dfe9d2 70%,#aacbe8)"></div>
  <svg class="abs" style="left:650px;top:103px" width="44" height="58" viewBox="0 0 44 58"><path d="M22 2a20 20 0 0 0-20 20c0 15 20 34 20 34s20-19 20-34A20 20 0 0 0 22 2z" fill="#f47c9c"/><circle cx="22" cy="21" r="7" fill="#fff"/></svg>
</section>

<section class="section newsletter">
  <div class="abs newsletter-text">Sign Up For Latest News &amp; Promotions with Lumeria</div>
  <div class="abs news-input">Your Email Address</div>
  <div class="abs news-btn">Subscribe</div>
</section>

<footer class="section site-footer">
  <div class="abs footer-brand">Lumeria</div>
  <p class="abs footer-about">Lorem Ipsum is simply dummy text of the printing and typesetting industry. Lorem Ipsum has been the industry's standard dummy text ever since the 1500s, when an unknown printer took a galley.</p>
  <div class="abs social" style="left:137px"></div>
  <div class="abs social" style="left:170px"></div>
  <div class="abs social" style="left:203px"></div>
  <div class="abs social" style="left:236px"></div>
  <div class="abs social" style="left:269px"></div>
  <div class="abs social" style="left:302px"></div>
  <div class="abs social" style="left:335px"></div>
  <div class="abs social" style="left:368px"></div>

  <div class="abs footer-heading" style="left:566px">Navigation</div>
  <div class="abs footer-nav">› Home<br>› About Us<br>› Blogs<br>› Services<br>› Contact Us</div>

  <div class="abs footer-heading" style="left:856px">Latest Post</div>
  <div class="img-fill avatar" role="img" aria-label="Post thumbnail" style="left:856px;top:110px;width:58px;height:58px;background:#c9a090"></div>
  <div class="abs post-date" style="left:932px;top:110px">June 7, 2016</div>
  <div class="abs post-text" style="left:932px;top:128px">It is a long established fact<br>that a reader will be</div>
  <div class="img-fill avatar" role="img" aria-label="Post thumbnail" style="left:856px;top:189px;width:58px;height:58px;background:#d8b4a4"></div>
  <div class="abs post-date" style="left:932px;top:189px">June 7, 2016</div>
  <div class="abs post-text" style="left:932px;top:207px">It is a long established fact<br>that a reader will be</div>
  <div class="img-fill avatar" role="img" aria-label="Post thumbnail" style="left:856px;top:268px;width:58px;height:58px;background:#b48c7c"></div>
  <div class="abs post-date" style="left:932px;top:268px">June 7, 2016</div>
  <div class="abs post-text" style="left:932px;top:286px">It is a long established fact<br>that a reader will be</div>
</footer>
<div class="section copyright">Copyright 2016 Lumeria Salon All Rights Reserved</div>

</body>
</html>
```